Need Help having my business card stand out

I am the owner of Pine Ridge Canine Coaching and would like for my business cards to stand out. I have been trying to keep designing them myself but I can't get what I have in my head on the card. I will try my best to post templates that I like for inspirations. I want something unique but elegant. I don't want in to look cartoony or cheesy. It needs to pop in a pet shop but also in a coffee shop or gym.

Target Market(s)

Dog owners, Married ,No young kids Jr High school kids and up (maybe kids on the way) Executives, Stay at home moms/wives, Small business owners

Industry/Entity Type

Dog Training

Contact Information for Business Card

Trevor Holloway, 555-304-7162, info@pineridgecanine.example, www.pineridgecanine.example

Colors

Designer to choose colors to be used in the design.

Requirements
Must have
• my logo
Should not have
• Cursive lettering

```html
<!DOCTYPE html>
<html lang="en">
<head>
<meta charset="utf-8">
<title>Pine Ridge Canine Coaching – Business Card</title>
<link href="https://fonts.googleapis.com/css2?family=Open+Sans:wght@300;400;600&display=swap" rel="stylesheet">
<style>
  :root {
    --backdrop: #e4e3df;
    --card: #1f1f20;
    --card-edge: #151516;
    --gold: #c9b88e;
    --gold-soft: #a89a76;
    --gold-deep: #8d7f5d;
    --ink: #1f1f20;
  }
  html, body {
    margin: 0;
    padding: 0;
    width: 1200px;
    height: 1021px;
    overflow: hidden;
    background: var(--backdrop);
    font-family: "Open Sans", Arial, sans-serif;
  }
  .canvas {
    position: relative;
    width: 1200px;
    height: 1021px;
  }
  .card {
    position: absolute;
    left: 220px;
    width: 760px;
    height: 434px;
    background: var(--card);
    box-shadow: 0 6px 18px rgba(0,0,0,.25);
    color: var(--gold);
  }
  .card--front { top: 51px; }
  .card--back { top: 536px; }

  .brand-seal {
    position: absolute;
    border-radius: 50%;
    background: radial-gradient(circle at 35% 30%, #e2d6b6 0%, var(--gold) 45%, var(--gold-deep) 100%);
    display: flex;
    align-items: center;
    justify-content: center;
    text-align: center;
  }
  .brand-seal__name {
    color: var(--ink);
    font-weight: 600;
    text-transform: uppercase;
    letter-spacing: 1px;
    line-height: 1.25;
  }
  .card--front .brand-seal {
    width: 220px; height: 220px;
    left: 270px; top: 58px;
  }
  .card--front .brand-seal__name { font-size: 21px; width: 160px; }

  .front-tagline {
    position: absolute;
    left: 0; right: 0;
    top: 300px;
    text-align: center;
    font-size: 17px;
    font-weight: 400;
    letter-spacing: .5px;
    line-height: 1.55;
    color: var(--gold-soft);
  }

  .card--back .brand-seal {
    width: 170px; height: 170px;
    right: 50px; top: 38px;
  }
  .card--back .brand-seal__name { font-size: 16px; width: 124px; }

  .holder-name {
    position: absolute;
    left: 52px; top: 232px;
    font-size: 32px;
    font-weight: 300;
    color: var(--gold);
  }
  .rule {
    position: absolute;
    left: 52px; right: 50px;
    top: 284px;
    height: 1.5px;
    background: linear-gradient(90deg, var(--gold-deep), #e6d9b6, var(--gold));
  }
  .holder-title {
    position: absolute;
    left: 52px; top: 294px;
    font-size: 17px;
    font-weight: 300;
    color: var(--gold-soft);
  }
  .contact-row {
    position: absolute;
    left: 52px; right: 50px;
    top: 352px;
    display: flex;
    justify-content: space-between;
    font-size: 16px;
    color: var(--gold);
  }
  .contact-item {
    display: flex;
    align-items: center;
    gap: 8px;
  }
  .contact-item svg { width: 18px; height: 18px; fill: none; stroke: var(--gold); stroke-width: 1.6; }
</style>
</head>
<body>
<main class="canvas">

  <section class="card card--front" aria-label="Card front">
    <div class="brand-seal">
      <span class="brand-seal__name">Pine Ridge Canine Coaching</span>
    </div>
    <p class="front-tagline">Pine Ridge Canine Coaching - CEDAR HOLLOW, TX<br>YOUR DOG TRAINER FOR LIFE!</p>
  </section>

  <section class="card card--back" aria-label="Card back">
    <div class="brand-seal">
      <span class="brand-seal__name">Pine Ridge Canine Coaching</span>
    </div>
    <div class="holder-name">Trevor Holloway</div>
    <div class="rule"></div>
    <div class="holder-title">Job Title</div>
    <div class="contact-row">
      <span class="contact-item">
        <svg viewBox="0 0 20 20" aria-hidden="true"><path d="M5 2h3l1.5 4-2 1.5a10 10 0 0 0 5 5l1.5-2 4 1.5v3a2 2 0 0 1-2 2A15 15 0 0 1 3 4a2 2 0 0 1 2-2z"/></svg>
        555-304-7162
      </span>
      <span class="contact-item">
        <svg viewBox="0 0 20 20" aria-hidden="true"><rect x="2" y="4.5" width="16" height="11"/><path d="M2 4.5l8 6.5 8-6.5"/></svg>
        info@pineridgecanine.example
      </span>
      <span class="contact-item">
        <svg viewBox="0 0 20 20" aria-hidden="true"><circle cx="10" cy="10" r="8"/><ellipse cx="10" cy="10" rx="3.5" ry="8"/><path d="M2 10h16"/></svg>
        www.pineridgecanine.example
      </span>
    </div>
  </section>

</main>
</body>
</html>
```